Holiday Rental Company Flyer Design (DL not A5)

Project Brief:
We need a double sided DL flyer designed for an up market Holiday Rental Company that portrays a personalised approach to property management. These are to be used for letter box drops to homes we're specifically targeting so the design should be modern, complimentary colour palette, uncluttered & visually appealing.

Please Download the DL Template from Quillmark here: http://www.quillmark-example.com.au/vp/ns/propath/UploadResources.aspx?selectedTab=0?pfid=BFB&pf_id=BFB&xnav=easypath-upload-image#Templates

Target Market(s)

Wealthy Home Owners

Industry/Entity Type

It Company

Font styles to use
Other font styles liked:
• Avant Garde Extra Light & Demi

Colors
33b8a4

Requirements
Must have
• DL Flyer sizes (210mm width x 99mm width, plus 3mm bleed)
• Front: Logo, Main Image & Grab
• Back: Contact Details & Brief Description of our business
• Images: Ideally the main image should be the house with the pool but alternatively a lifestyle images could also be used.
Nice to have
• A creative designer!
Should not have
• Clutter & busy designs

```html
<!DOCTYPE html>
<html lang="en">
<head>
<meta charset="utf-8">
<title>Harbourline Stays – DL Flyer</title>
<link rel="stylesheet" href="https://fonts.googleapis.com/css2?family=Poppins:wght@200;300;600&display=swap">
<style>
  :root {
    --canvas: #ffffff;
    --card-front: #646464;
    --card-back: #5f6060;
    --ink-light: #e6e6e6;
    --ink-soft: #cfcfcf;
    --ink-strong: #ffffff;
    --sky-top: #2b3f8a;
    --sky-low: #5a6fb0;
    --facade: #8c93a8;
    --timber: #7a3f22;
    --pool: #3fa8f0;
    --pool-glow: #8fe0ff;
  }
  * { margin: 0; padding: 0; box-sizing: border-box; }
  html, body {
    width: 1200px; height: 900px; overflow: hidden;
    background: var(--canvas);
    font-family: "Poppins", "Century Gothic", sans-serif;
  }
  .stage { position: relative; width: 1200px; height: 900px; }

  .flyer { position: absolute; color: var(--ink-light); text-align: center; }
  .flyer--front { left: 204px; top: 92px; width: 338px; height: 716px; background: var(--card-front); }
  .flyer--back  { left: 647px; top: 86px; width: 348px; height: 727px; background: var(--card-back); }

  .brand { position: absolute; left: 0; right: 0; display: flex; flex-direction: column; align-items: center; }
  .brand__name {
    font-weight: 200; font-size: 17px; line-height: 17px;
    letter-spacing: 1.6px; text-transform: uppercase; color: var(--ink-light);
  }
  .brand__mark { margin-top: 10px; width: 18px; height: 18px; border: 1px solid var(--ink-light); border-radius: 50%; }
  .flyer--front .brand { top: 26px; }
  .flyer--back .brand { top: 64px; }

  .hero-image {
    position: absolute; left: 0; top: 121px; width: 338px; height: 545px;
    background:
      radial-gradient(ellipse 70% 22% at 60% 88%, var(--pool-glow), transparent 70%),
      linear-gradient(180deg, var(--sky-top) 0%, var(--sky-low) 18%, var(--facade) 40%, #6d6c78 58%, var(--timber) 68%, #5a5a5e 74%, var(--pool) 84%, #2a7fd0 100%);
  }

  .tagline {
    position: absolute; left: 0; right: 0;
    font-weight: 300; font-size: 6.5px; letter-spacing: 0.2px; color: var(--ink-soft);
  }
  .flyer--front .tagline { top: 688px; }
  .flyer--back .tagline { top: 668px; }

  .intro-heading {
    position: absolute; left: 0; right: 0; top: 176px;
    font-weight: 200; font-size: 12.5px; color: var(--ink-light);
  }
  .intro {
    position: absolute; left: 20px; right: 20px; top: 226px;
    font-weight: 200; font-size: 7.6px; line-height: 17px; color: var(--ink-soft);
  }
  .intro p + p { margin-top: 17px; }

  .contact {
    position: absolute; left: 0; right: 0; top: 496px;
    list-style: none; font-weight: 600; font-size: 8.6px; line-height: 17px; color: var(--ink-strong);
  }
</style>
</head>
<body>
<main class="stage">

  <section class="flyer flyer--front" aria-label="Flyer front">
    <div class="brand">
      <span class="brand__name">Harbourline</span>
      <span class="brand__name">Stays</span>
      <span class="brand__mark" aria-hidden="true"></span>
    </div>
    <div class="hero-image" role="img" aria-label="Modern architect-designed holiday home at dusk with lit windows, timber wall and glowing blue pool"></div>
    <p class="tagline">Holiday Rental Management with a difference</p>
  </section>

  <section class="flyer flyer--back" aria-label="Flyer back">
    <div class="brand">
      <span class="brand__name">Harbourline</span>
      <span class="brand__name">Stays</span>
      <span class="brand__mark" aria-hidden="true"></span>
    </div>
    <h2 class="intro-heading">What we do differently!</h2>
    <div class="intro">
      <p>Rather than relying upon a key safe or a central pickup destination,<br>a ‘Harbourline Stays’ staff member will greet guests upon arrival.</p>
      <p>Our ‘Meet &amp; Greet’ service provides home owners with a<br>n increased level of Security and also allows us to:</p>
      <p>Prepare the home for their arrival (lights, heaters, music etc.)<br>Establish a rapport &amp; help facilitate future bookings<br>Reiterate their responsibilities to ensure the return of their bond</p>
      <p>If you’d like to know what your property could<br>achieve or require additional information,<br>please contact us on:</p>
    </div>
    <ul class="contact">
      <li>t: (03)5900 1234</li>
      <li>e: stay@harbourlinestays.com.au</li>
      <li>w: harbourlinestays.com.au</li>
      <li>PO Box 48, Saltmere Victoria 3990</li>
    </ul>
    <p class="tagline">Holiday Rental Management with a difference</p>
  </section>

</main>
</body>
</html>
```